New Wordpress Design Project

The website is my name tessamarlowgrant.com

I need a website design that will be graphically pleasing and have a crisp feel to it. I am a business and personal coach and have many different niches that I work with. I am looking for the central site to describe who I am and how I help people - I help people "wake up" to make conscious choices in their lives. I use hypnosis but do not want it to be esoteric, I ground the hypnosis and base it in science of how people can manage their state to reach their full potential in their lives and in business. I work one on one but also do public speaking and recently started to do trainings with corporations, helping people improve their business. I am looking at this as a merge of hypnosis and other tools with the business or corporate world - based in science - neuroplasticity, brain training etc. I will be helping people to overcome anxiety and stress, limiting beliefs, controlling and choosing habits that will work for them, fears and phobias, golf/sports improvement, weight loss.

Really helping people to center back with themselves, to not be so caught up in their head but drop into their heart and with what is really going on. My mission is to connect them back with themselves, using language, state and conscious choice.

I work online with entrepreneurs helping them to get unstuck, move past fears and limiting beliefs to create the business of their dreams.

I added a file of what I am envisioning on the right hand side of my site to show people the different niches I am involved with.

Some sites that I like www.brindaquell.com www.corabethwynn.org http://www.devoratusk.com/ , Details for my new Wordpress Design Project will be added soon. , The website is my name tessamarlowgrant.com

the square boxes graphic below is similar to one that I will be making for a page on my site for clarity and crispness. But will be creating it more in the teal color.

Target Market(s)

My target market are both male and female 30-50 either entreprenuers/business people

Industry/Entity Type

Training

Requirements
Must have
• A video with an opt in box
My background color is teal/blue (see below file)
Social media links

```html
<!DOCTYPE html>
<html lang="en">
<head>
<meta charset="utf-8">
<title>TessaMarlowGrant — Optimizing Your Mindset for Entrepreneurial Success</title>
<link rel="stylesheet" href="https://fonts.googleapis.com/css2?family=Lobster&family=Open+Sans:ital,wght@0,400;0,600;0,700;1,400&display=swap">
<style>
:root{
  --frame:#4f5152;
  --teal:#12a4a9;
  --teal-deep:#0b8b91;
  --teal-light:#4fd0d2;
  --teal-input:#9be6e6;
  --link:#18a6ad;
  --band:#d8d9da;
  --white:#ffffff;
  --ink:#3a3a3a;
  --muted:#777a7c;
  --rule:#e2e4e5;
  --box:#f1f2f2;
  --box-edge:#dcdedf;
  --footer:#3a3b3c;
  --footer-deep:#2b2c2d;
  --footer-text:#b9bbbc;
  --yellow:#f3e22c;
}
*{box-sizing:border-box;margin:0;padding:0}
html,body{width:1200px;height:2273px;overflow:hidden}
body{background:var(--frame);font-family:"Open Sans",Arial,sans-serif;color:var(--ink);position:relative}
.sheet{position:absolute;left:41px;top:18px;width:1118px;height:2237px;background:var(--white);overflow:hidden}
.abs{position:absolute}

/* header */
.header{left:0;top:0;width:1118px;height:494px;
  background:radial-gradient(ellipse at 50% 30%,#2ec3c6 0%,var(--teal) 45%,var(--teal-deep) 100%)}
.header::before{content:"";position:absolute;left:0;top:0;right:0;height:8px;background:var(--teal-light);opacity:.6}
.brand{left:154px;top:18px;display:flex;align-items:center;gap:12px}
.brand-dot{width:40px;height:40px;border-radius:50%;background:var(--teal-light)}
.brand-name{font-weight:700;font-size:31px;color:var(--white);letter-spacing:.3px;line-height:1}
.tagline{left:206px;top:58px;font-size:11.5px;color:#0d5e63;font-style:italic}
.nav{left:577px;top:95px;display:flex;gap:26px;font-size:12.5px;color:#dff6f6}
.nav a{color:inherit;text-decoration:none}
.nav .active{color:var(--white);font-weight:600}
.nav-rule{left:154px;top:122px;width:806px;height:1px;background:rgba(255,255,255,.25)}

.video{left:154px;top:187px;width:396px;height:240px;border-radius:3px;
  background:linear-gradient(135deg,#3f5a2a 0%,#8fa25b 40%,#d8c3a0 60%,#4d6130 100%);
  box-shadow:0 4px 10px rgba(0,0,0,.25)}
.video svg{position:absolute;left:168px;top:90px}
.video-caption{position:absolute;left:0;bottom:0;width:100%;padding:8px 12px;font-size:11px;color:var(--white);background:linear-gradient(transparent,rgba(0,0,0,.55))}
.hero-title{left:591px;top:192px;font-family:"Lobster",cursive;font-size:33px;color:var(--white);line-height:1}
.hero-text{left:591px;top:236px;width:370px;font-size:11.5px;line-height:17px;color:#e9fbfb;font-weight:600}
.field{left:591px;width:318px;height:28px;background:var(--teal-input);border:1px solid #c5f2f2;font-size:11px;color:#3c9fa2;padding:6px 10px}
.submit{left:591px;top:396px;width:107px;height:30px;border-radius:3px;background:linear-gradient(#f9ee62,var(--yellow));border:1px solid #c9b814;font-size:12px;color:#4f4a10;text-align:center;line-height:28px}
.arrow{width:26px;height:26px;border-radius:50%;background:rgba(0,0,0,.22)}
.arrow svg{display:block;margin:7px auto}

.band{left:0;top:494px;width:1118px;height:45px;background:var(--band)}
.dots{left:512px;top:516px;display:flex;gap:14px}
.dots span{width:11px;height:11px;border-radius:50%;background:#9b9d9f}

/* posts */
.post{left:154px;width:510px}
.post-title{font-family:"Lobster",cursive;font-size:22px;color:#2f3132;font-weight:400;line-height:1.1}
.post-meta{margin-top:8px;font-size:10.5px;color:var(--muted);font-style:italic}
.post-meta a{color:var(--link);text-decoration:none;font-style:normal}
.post-body{display:flex;gap:18px;margin-top:16px}
.thumb{flex:0 0 150px;height:148px;border:1px solid var(--box-edge);padding:5px;background:var(--white)}
.thumb div{width:100%;height:100%}
.post-text{font-size:11.2px;line-height:16.4px;color:#6b6e70}
.post-foot{display:flex;justify-content:space-between;align-items:flex-start;margin-top:10px;padding-bottom:12px;border-bottom:1px solid var(--rule)}
.post-tags{font-size:10.5px;line-height:14px;color:var(--muted);font-style:italic}
.post-tags a{color:var(--link);text-decoration:none}
.more{width:86px;height:22px;border-radius:3px;background:#e3e4e5;border:1px solid #cfd1d2;font-size:10.5px;color:#6b6e70;text-align:center;line-height:20px}

/* sidebar */
.banner{left:727px;width:234px;height:73px;border-radius:3px;box-shadow:0 2px 4px rgba(0,0,0,.2)}
.widget{left:727px;width:234px;background:var(--box);border:1px solid var(--box-edge);border-radius:3px;padding:16px 14px}
.widget h3{font-family:"Lobster",cursive;font-weight:400;font-size:19px;color:#2f3132;padding-bottom:10px;border-bottom:1px solid var(--box-edge);margin-bottom:16px}
.about{display:flex;gap:12px}
.about-photo{flex:0 0 58px;height:58px;border:3px solid var(--white);background:linear-gradient(135deg,#c8a27a,#7d6a3e);box-shadow:0 1px 2px rgba(0,0,0,.2)}
.about p{font-size:11px;line-height:16.5px;color:#6b6e70}
.widget .link{display:block;margin-top:10px;font-size:11px;color:var(--link)}
.recent li{list-style:none;display:flex;gap:10px;font-size:11px;line-height:16px;margin-bottom:13px}
.recent li svg{flex:0 0 14px;margin-top:2px}
.recent a{color:var(--link);display:block}
.recent span{color:#6b6e70}

/* footer */
.footer{left:0;top:1864px;width:1118px;height:373px;background:radial-gradient(ellipse at 50% 0%,#4a4b4c 0%,var(--footer) 55%,var(--footer-deep) 100%)}
.f-col{top:70px}
.f-col h4{font-family:"Lobster",cursive;font-weight:400;font-size:19px;color:var(--white);padding-bottom:10px;border-bottom:1px solid #55575a;margin-bottom:16px}
.f-col p{font-size:11px;line-height:19px;color:var(--footer-text)}
.f-list li{list-style:none;display:flex;gap:10px;font-size:11px;line-height:15px;color:var(--footer-text);margin-bottom:12px}
.f-help{display:flex;gap:12px}
.f-help-img{flex:0 0 50px;height:50px;border:3px solid #e8e8e8;background:linear-gradient(135deg,#3bb0c4,#9fd8c6)}
.copyright{left:0;top:320px;width:1118px;height:53px;background:var(--footer-deep);border-top:1px solid #444;font-size:10px;color:#8d8f91;text-align:center;line-height:30px}
</style>
</head>
<body>
<div class="sheet">

  <header class="header abs">
    <div class="brand abs"><span class="brand-dot"></span><span class="brand-name">TessaMarlowGrant</span></div>
    <div class="tagline abs">Optimizing Your Mindset for Entrepreneurial Success</div>
    <nav class="nav abs">
      <a class="active">Home »</a><a>Blog »</a><a>About Me »</a><a>Contact Me »</a><a>List of Books »</a>
    </nav>
    <div class="nav-rule abs"></div>

    <div class="arrow abs" style="left:88px;top:294px"><svg width="12" height="12" viewBox="0 0 12 12"><path d="M8 1L3 6l5 5" fill="none" stroke="#fff" stroke-width="2"/></svg></div>
    <div class="arrow abs" style="left:1004px;top:294px"><svg width="12" height="12" viewBox="0 0 12 12"><path d="M4 1l5 5-5 5" fill="none" stroke="#fff" stroke-width="2"/></svg></div>

    <div class="video abs" role="img" aria-label="Welcome video still of the coach outdoors among green leaves">
      <svg width="62" height="62" viewBox="0 0 62 62"><circle cx="31" cy="31" r="30" fill="rgba(255,255,255,.45)"/><path d="M24 18l20 13-20 13z" fill="#fff"/></svg>
      <div class="video-caption">Lorem ipsum dolor sit amet, consectetur adipiscing elit...</div>
    </div>

    <div class="hero-title abs">Lorem ipsum dolor sit amet...</div>
    <p class="hero-text abs">Lorem ipsum dolor sit amet, consectetur adipiscing elit, sed do eiusmod tempor incididunt ut labore et dolore magna. Ut enim ad minim veniam, quis nostrud exercitation ullamco laboris...</p>
    <div class="field abs" style="top:301px">Your Name</div>
    <div class="field abs" style="top:346px">Email Address</div>
    <div class="submit abs">Submit</div>
  </header>

  <div class="band abs"></div>
  <div class="dots abs"><span></span><span></span><span></span></div>

  <article class="post abs" style="top:610px">
    <h2 class="post-title">Ut rutrum tortor in scelerisque mollis.</h2>
    <div class="post-meta">✎ Written by <a>TESSA MARLOW</a> on December 7, 2012 | 💬 <a>436 comments</a></div>
    <div class="post-body">
      <div class="thumb"><div role="img" aria-label="Colourful painted hand reaching upward" style="background:linear-gradient(135deg,#6cc7c9,#e0a04a 55%,#c44a3a)"></div></div>
      <p class="post-text">Duis aute irure dolor in reprehenderit in voluptate velit esse cillum dolore eu fugiat nulla pariatur. Excepteur sint occaecat cupidatat non proident, sunt in culpa qui officia deserunt mollit anim id est laborum. Sed ut perspiciatis unde omnis iste natus error sit voluptatem accusantium doloremque laudantium, totam rem aperiam, eaque ipsa quae ab illo inventore veritatis et quasi architecto beatae vitae dicta sunt explicabo. Nemo enim ipsam voluptatem quia voluptas sit aspernatur aut odit aut fugit.</p>
    </div>
    <div class="post-foot">
      <div class="post-tags">Categories: <a>Limiting Beliefs</a><br>Tags: <a>Beliefs, change, desire, money.</a></div>
      <div class="more">Read More</div>
    </div>
  </article>

  <article class="post abs" style="top:906px">
    <h2 class="post-title">Vivamus ut dui eget sem bibendum consectetur</h2>
    <div class="post-meta">✎ Written by <a>TESSA MARLOW</a> on December 7, 2012 | 💬 <a>436 comments</a></div>
    <div class="post-body">
      <div class="thumb"><div role="img" aria-label="Black and white portrait in a knitted hat" style="background:linear-gradient(135deg,#d6d6d6,#8a8a8a)"></div></div>
      <p class="post-text">Sed ut perspiciatis unde omnis iste natus error sit voluptatem accusantium doloremque laudantium, totam rem aperiam, eaque ipsa quae ab illo inventore veritatis et quasi architecto beatae vitae dicta sunt explicabo. Nemo enim ipsam voluptatem quia voluptas sit aspernatur aut odit aut fugit, sed quia consequuntur magni dolores eos qui ratione voluptatem sequi nesciunt. Neque porro quisquam est, qui dolorem ipsum quia dolor sit amet, consectetur, adipisci velit, sed quia non.</p>
    </div>
    <div class="post-foot">
      <div class="post-tags">Categories: <a>Limiting Beliefs</a><br>Tags: <a>Beliefs, change, desire, money.</a></div>
      <div class="more">Read More</div>
    </div>
  </article>

  <article class="post abs" style="top:1212px">
    <h2 class="post-title">Cras blandit nisi sit amet suscipit dictum</h2>
    <div class="post-meta">✎ Written by <a>TESSA MARLOW</a> on December 7, 2012 | 💬 <a>436 comments</a></div>
    <div class="post-body">
      <div class="thumb"><div role="img" aria-label="Line sketch of a figure with open arms" style="background:linear-gradient(135deg,#f2f4f6,#c9d4dc)"></div></div>
      <p class="post-text">Totam rem aperiam, eaque ipsa quae ab illo inventore veritatis et quasi architecto beatae vitae dicta sunt explicabo. Nemo enim ipsam voluptatem quia voluptas sit aspernatur aut odit aut fugit, sed quia consequuntur magni dolores eos qui ratione voluptatem sequi nesciunt. Neque porro quisquam est, qui dolorem ipsum quia dolor sit amet, consectetur, adipisci velit, sed quia non numquam eius modi tempora incidunt ut labore et dolore magnam aliquam quaerat voluptatem.</p>
    </div>
    <div class="post-foot">
      <div class="post-tags">Categories: <a>Limiting Beliefs</a><br>Tags: <a>Beliefs, change, desire, money.</a></div>
      <div class="more">Read More</div>
    </div>
  </article>

  <article class="post abs" style="top:1515px">
    <h2 class="post-title">Quisque non faucibus nisi.</h2>
    <div class="post-meta">✎ Written by <a>TESSA MARLOW</a> on December 7, 2012 | 💬 <a>436 comments</a></div>
    <div class="post-body">
      <div class="thumb"><div role="img" aria-label="Close-up of yellow and green leaves" style="background:linear-gradient(135deg,#3d4a14,#b9a524 50%,#4e5a1a)"></div></div>
      <p class="post-text">Sit voluptatem accusantium doloremque laudantium, totam rem aperiam, eaque ipsa quae ab illo inventore veritatis et quasi architecto beatae vitae dicta sunt explicabo. Nemo enim ipsam voluptatem quia voluptas sit aspernatur aut odit aut fugit, sed quia consequuntur magni dolores eos qui ratione voluptatem sequi nesciunt. Neque porro quisquam est, qui dolorem ipsum quia dolor sit amet, consectetur, adipisci velit, sed quia non numquam eius modi tempora in.</p>
    </div>
    <div class="post-foot">
      <div class="post-tags">Categories: <a>Limiting Beliefs</a><br>Tags: <a>Beliefs, change, desire, money.</a></div>
      <div class="more">Read More</div>
    </div>
  </article>

  <aside>
    <div class="banner abs" style="top:609px;background:linear-gradient(90deg,#5a1a22,#c2384a 60%,#7a2030)" role="img" aria-label="Banner: overcome fear and self doubt"></div>
    <div class="banner abs" style="top:705px;background:linear-gradient(90deg,#1d2a0c,#4e7a18 60%,#22300e)" role="img" aria-label="Banner: get more done in less time"></div>
    <div class="banner abs" style="top:803px;background:linear-gradient(90deg,#0f2a0e,#2f7a24 60%,#142e10)" role="img" aria-label="Banner: my Halvorsen interview"></div>

    <section class="widget abs" style="top:925px;height:303px">
      <h3>About Tessa Marlow...</h3>
      <div class="about">
        <div class="about-photo" role="img" aria-label="Portrait photo of the coach"></div>
        <p>I am an entrepreneur and coach. I help you get your Inner-Game working so you have Outer-Game success! I have an obsession with the mechanics of our thoughts and actions and the neuroscience behind it.</p>
      </div>
      <a class="link">Read more »</a>
    </section>

    <section class="widget abs" style="top:1271px;height:393px">
      <h3>Recent Articles</h3>
      <ul class="recent">
        <li><svg width="14" height="12" viewBox="0 0 14 12"><path d="M1 11L11 3M7 2l5 0 0 5" fill="none" stroke="#555" stroke-width="1.8"/></svg><div><a>Dolore magna aliqua!</a><span>Morbi sodales, risus non nibh luctus nulla, rutrum...</span></div></li>
        <li><svg width="14" height="12" viewBox="0 0 14 12"><path d="M1 11L11 3M7 2l5 0 0 5" fill="none" stroke="#555" stroke-width="1.8"/></svg><div><a>Veniam, quis nostrudmetus...</a><span>Maecenas et felis metus. Donec libero tincidunt in.</span></div></li>
        <li><svg width="14" height="12" viewBox="0 0 14 12"><path d="M1 11L11 3M7 2l5 0 0 5" fill="none" stroke="#555" stroke-width="1.8"/></svg><div><a>Exercitation ullamco laboris...</a><span>In enim id est laborum. Sed ut perspiciatis unde.</span></div></li>
        <li><svg width="14" height="12" viewBox="0 0 14 12"><path d="M1 11L11 3M7 2l5 0 0 5" fill="none" stroke="#555" stroke-width="1.8"/></svg><div><a>Dolore magna aliqua!</a><span>Morbi sodales, risus non nibh luctus nulla, rutrum...</span></div></li>
        <li><svg width="14" height="12" viewBox="0 0 14 12"><path d="M1 11L11 3M7 2l5 0 0 5" fill="none" stroke="#555" stroke-width="1.8"/></svg><div><a>Veniam, quis nostrudmetus...</a><span>Maecenas et felis metus. Donec libero tincidunt in.</span></div></li>
      </ul>
    </section>
  </aside>

  <footer class="footer abs">
    <div class="f-col abs" style="left:154px;width:236px">
      <h4>Coaching Sessions</h4>
      <p>I offer one on one coaching as well as group coaching. If you want to accelerate your success then coaching sessions are the best way to accomplish that. I really enjoy working with my clients and seeing them become and achieve what they want in life. Find out more here...</p>
    </div>
    <div class="f-col abs" style="left:427px;width:236px">
      <h4>Launch Your Passion</h4>
      <ul class="f-list">
        <li><svg width="14" height="12" viewBox="0 0 14 12"><path d="M1 11L11 3M7 2l5 0 0 5" fill="none" stroke="#ccc" stroke-width="1.8"/></svg>Dolore magna aliqua. Ut enim ad minim</li>
        <li><svg width="14" height="12" viewBox="0 0 14 12"><path d="M1 11L11 3M7 2l5 0 0 5" fill="none" stroke="#ccc" stroke-width="1.8"/></svg>Veniam, quis nostrud</li>
        <li><svg width="14" height="12" viewBox="0 0 14 12"><path d="M1 11L11 3M7 2l5 0 0 5" fill="none" stroke="#ccc" stroke-width="1.8"/></svg>Exercitation ullamco laboris nisi ut aliquip</li>
        <li><svg width="14" height="12" viewBox="0 0 14 12"><path d="M1 11L11 3M7 2l5 0 0 5" fill="none" stroke="#ccc" stroke-width="1.8"/></svg>Ea commodo consequat. Duis irure...</li>
        <li><svg width="14" height="12" viewBox="0 0 14 12"><path d="M1 11L11 3M7 2l5 0 0 5" fill="none" stroke="#ccc" stroke-width="1.8"/></svg>In reprehenderit in  fugiat nulla pariatur...</li>
      </ul>
    </div>
    <div class="f-col abs" style="left:702px;width:256px">
      <h4>Help You Succeed!</h4>
      <div class="f-help">
        <div class="f-help-img" role="img" aria-label="Small colourful painted hand thumbnail"></div>
        <p>Lorem ipsum dolor sit amet, consectetur adipisicing elit, sed do eiusmod tempor incididunt ut labore et dolore magna aliqua. Ut enim ad minim veniam, quis nostrud exercitation ullamco laboris nisi ut irure dolor in reprehenderit ...</p>
      </div>
    </div>
    <div class="copyright abs">Copyright © 2014 TessaMarlowGrant.com</div>
  </footer>

</div>
</body>
</html>
```